3D Buchcover für ebook
Das Design kam überraschend und war quasi aus dem Stand perfekt. Ich konnte gar nicht anders, als es zum Gewinner zu küren.
Zielgruppe
Das Buch erscheint als ebook, später auch als gedruckte Version. Es spricht Personen an, die mittels einer Diät nicht nur ihre Figur, sondern auch ihre Gesundheit, Fitneß und das Aussehen im Allgemeinen verbessern wollen. Die Hauptzielgruppe sind Frauen zwischen 35 und 60+.
Branche: Medizin/Gesundheit.
Aufgabenstellung
Hergestellt werde soll das Cover für ein ebook mit dem Titel "Der stille Spiegel als klare Antwort". Außerdem soll folgende Headline untegebracht werden: "Rückblick auf 11 Monate Alltag mit Suppe". Es soll ein Bild der Autorin verwendet werden. Aus den gelieferten Vorlagen kann die Frauenfigur ausgeschnitten werden. Wichtig ist, ihre Figur und die Ausstrahlung wirkungsvoll zur Geltung zu bringen. Unter den mitgelieferten Deteien ist außerdem das aktuelle Cover enthalten (das Buch ist bereits veröffentlicht). Auch der Autorname "Wiebke Lanzig" soll auf dem Cover Platz finden.
Das Cover soll auch im Kleinformat, wie es üblicherweise in den Suchergebnissen auf Buchwelle angezeigt wird, eine Aussagekraft besitzen.

```html
<!DOCTYPE html>
<html lang="de">
<head>
<meta charset="utf-8">
<title>Der stille Spiegel als klare Antwort – Cover</title>
<link href="https://fonts.googleapis.com/css2?family=Anton&family=Nothing+You+Could+Do&family=Homemade+Apple&display=swap" rel="stylesheet">
<style>
  :root {
    --page-bg: #dfeaf6;
    --denim-dark: #2a3c5c;
    --denim-mid: #4d6185;
    --denim-light: #7b8daa;
    --portrait-skin: #c9a08a;
    --portrait-top: #1c2033;
    --portrait-jeans: #2b3f78;
    --title-white: #ffffff;
    --title-red: #ee2a2a;
    --label-paper: #d8ccb4;
    --label-ink: #2b2b4a;
    --subtitle-ink: #e9edf4;
  }
  html, body {
    margin: 0;
    width: 1112px;
    height: 1200px;
    overflow: hidden;
    background: var(--page-bg);
  }
  .cover {
    position: absolute;
    left: 156px;
    top: 50px;
    width: 800px;
    height: 1100px;
    overflow: hidden;
    box-shadow: 0 12px 40px rgba(30, 50, 80, 0.25);
  }
  .cover__denim {
    position: absolute;
    inset: 0;
    background:
      radial-gradient(ellipse at 35% 25%, var(--denim-light) 0%, transparent 55%),
      linear-gradient(180deg, var(--denim-mid) 0%, var(--denim-dark) 100%);
  }
  .cover__portrait {
    position: absolute;
    left: 390px;
    top: 80px;
    width: 410px;
    height: 1020px;
    background: linear-gradient(180deg,
      var(--portrait-skin) 0%, var(--portrait-skin) 38%,
      var(--portrait-top) 42%, var(--portrait-top) 68%,
      var(--portrait-jeans) 72%, var(--portrait-jeans) 100%);
    opacity: 0.85;
    border-radius: 160px 160px 0 0;
  }
  .cover__author-label {
    position: absolute;
    left: 190px;
    top: 198px;
    width: 232px;
    height: 80px;
    background: var(--label-paper);
    transform: rotate(-1deg);
    display: flex;
    align-items: center;
    justify-content: center;
    font-family: "Homemade Apple", cursive;
    font-size: 25px;
    color: var(--label-ink);
  }
  .cover__title {
    position: absolute;
    left: 106px;
    top: 470px;
    margin: 0;
    font-family: "Anton", sans-serif;
    font-weight: 400;
    font-size: 132px;
    line-height: 130px;
    text-transform: uppercase;
    color: var(--title-white);
    transform: rotate(-2.5deg);
    transform-origin: left top;
    text-shadow: 0 3px 10px rgba(0, 0, 0, 0.35);
    letter-spacing: -1px;
  }
  .cover__title-line { display: block; white-space: nowrap; }
  .cover__title-accent { color: var(--title-red); }
  .cover__subtitle {
    position: absolute;
    left: 110px;
    top: 1010px;
    margin: 0;
    font-family: "Nothing You Could Do", cursive;
    font-size: 32px;
    color: var(--subtitle-ink);
    transform: rotate(-2.5deg);
    transform-origin: left top;
    white-space: nowrap;
  }
</style>
</head>
<body>
  <div class="cover">
    <div class="cover__denim" role="img" aria-label="Jeansstoff mit Gesäßtasche als Hintergrund"></div>
    <div class="cover__portrait" role="img" aria-label="Foto der Autorin, sitzend in Trägertop und enger Jeans"></div>
    <div class="cover__author-label">Wiebke Lanzig</div>
    <h1 class="cover__title">
      <span class="cover__title-line">Der <span class="cover__title-accent">stille</span></span>
      <span class="cover__title-line"><span class="cover__title-accent">Spiegel</span></span>
      <span class="cover__title-line">als klare</span>
      <span class="cover__title-line">Antwort</span>
    </h1>
    <p class="cover__subtitle">Rückblick auf 11 Monate Alltag mit Suppe</p>
  </div>
</body>
</html>
```